Change logo on company documents

I want to change the logo on all company documents and change them company name that is written in certain places in the text.

Target Market(s)

Construction/Residential Home Remodeling

Colors

Designer to choose colors to be used in the design.

```html
<!DOCTYPE html>
<html lang="en">
<head>
<meta charset="utf-8">
<title>Harbor Ridge Roofing — Company Documents</title>
<link href="https://fonts.googleapis.com/css2?family=Open+Sans:wght@400;600;700&display=swap" rel="stylesheet">
<style>
:root{
  --bg:#dcdde0;
  --paper:#ffffff;
  --ink:#2a2a2a;
  --soft:#6b6b6b;
  --rule:#4a4a4a;
  --band:#cdbf85;
  --green:#2f6d3c;
  --blue:#1f5f8f;
}
*{box-sizing:border-box;margin:0;padding:0}
html,body{width:1200px;height:887px;overflow:hidden;background:var(--bg)}
body{position:relative;font-family:"Open Sans",Arial,sans-serif;color:var(--ink)}
.page{position:absolute;width:178px;background:var(--paper)}
.sheet{position:absolute;inset:7px;border:.6px solid var(--rule);padding:7px 8px;overflow:hidden}
.head{display:flex;justify-content:space-between;align-items:flex-start;height:24px}
.brand{display:flex;align-items:center;gap:2px;font-size:3.6px;font-weight:700;color:var(--ink);letter-spacing:.2px;margin-top:3px}
.mark{width:12px;height:12px;border:1.4px solid var(--ink);border-radius:50%}
.addr{font-style:normal;font-size:2.3px;line-height:1.4;text-align:right;color:var(--ink)}
.title{font-size:5.4px;font-weight:400;letter-spacing:.6px;text-align:center;margin:6px 0 8px}
.title.green{color:var(--ink)}
.sub{font-size:3.6px;letter-spacing:.4px;text-align:center;margin-bottom:6px}
p,li{font-size:2.4px;line-height:1.45}
p{margin-bottom:2.5px}
ol{padding-left:5px}
li{margin-bottom:2.5px}
.field{border-bottom:.4px solid var(--rule);height:7px;font-size:2.2px;color:var(--soft)}
.label{font-size:2.2px;color:var(--soft);padding-top:1px}
.row{display:flex;gap:14px}
.row>*{flex:1}
.sig{display:grid;grid-template-columns:1fr 1fr;gap:0 18px;margin-top:8px}
.sig div{border-top:.4px solid var(--rule);font-size:2.2px;padding-top:1px;height:14px}
.box{border:.4px solid var(--rule)}
.band{background:var(--band);font-size:2.3px;font-weight:700;padding:.6px 1.5px}
.note{font-size:2.3px;color:var(--green);font-style:italic;font-weight:600;text-align:center}
.notice-top{font-size:2.3px;color:var(--green);font-style:italic;font-weight:600;text-align:center;margin:2px 6px 6px}
.lined{display:grid;grid-template-columns:38% 62%;border:.4px solid var(--rule)}
.lined span{font-size:2.2px;border-bottom:.4px solid var(--rule);height:3.6px;padding-left:1px}
.lined span:nth-child(odd){background:var(--band);font-weight:700}
table{border-collapse:collapse;width:100%}
td,th{border:.4px solid var(--rule);font-size:2.2px;height:4px;padding:0 1px;text-align:left}
th{background:var(--band)}
.mat p{margin-bottom:1.8px}
.blue{color:var(--blue)}
.pnum{position:absolute;bottom:4px;right:14px;font-size:2.2px}
</style>
</head>
<body>

<!-- Row 1 -->
<section class="page" style="left:44px;top:56px;height:231px">
  <div class="sheet">
    <header class="head"><div class="brand"><span class="mark"></span>HARBOR RIDGE</div><address class="addr">412 LINDEN AVE STE B<br>RIVERTON, LA 70100<br>P: 555.010.2311<br>F: 555.010.9725</address></header>
    <h2 class="title">CERTIFICATE OF COMPLETION</h2>
    <div class="row"><div><div class="field"></div><div class="label">Homeowner</div></div><div><div class="field"></div><div class="label">Completion Date</div></div></div>
    <p style="margin-top:8px">I/We hereby certify that all necessary repairs as outlined in the contract between Harbor Ridge Roofing and ____________ located at ____________ have been completed in a satisfactory manner and all liens will be waived upon final payment for labor and materials.</p>
    <p>All contractors, subcontractors and suppliers who have provided labor or materials in connection with the repairs to the property have been paid in full or will be paid from the final invoice proceeds.</p>
    <div class="sig" style="margin-top:40px"><div>Client</div><div>Harbor Ridge Roofing</div><div>Date</div><div>Date</div></div>
  </div>
</section>

<section class="page" style="left:231px;top:56px;height:231px">
  <div class="sheet">
    <header class="head"><div class="brand"><span class="mark"></span>HARBOR RIDGE</div><address class="addr">412 LINDEN AVE STE B<br>RIVERTON, LA 70100<br>P: 555.010.2311<br>F: 555.010.9725</address></header>
    <h2 class="title">CHANGE ORDER</h2>
    <div class="row"><p>Job Name: ______________________</p><p>Date: ______________</p></div>
    <div class="row"><p>Job Location: ____________________</p><p>Terms: Due Upon Receipt</p></div>
    <p style="font-style:italic;font-weight:600;margin-top:3px">The following work/upgrades outlined below are changes to the scope specified on the original contract and/or insurance loss sheet. The homeowner acknowledges they are responsible for these additional costs.</p>
    <div class="box" style="height:56px"></div>
    <p style="text-align:right;margin-top:5px">Total Cost: ________________</p>
    <p style="margin-top:8px">By signing below the homeowner approves the additional work and/or upgrades and costs outlined above and agrees that payment for this change order is due upon signing of this agreement.</p>
    <div class="sig" style="margin-top:10px"><div>Homeowner</div><div>Harbor Ridge Roofing</div><div>Date</div><div>Date</div></div>
  </div>
</section>

<section class="page" style="left:417px;top:56px;height:231px">
  <div class="sheet">
    <header class="head"><div class="brand"><span class="mark"></span>HARBOR RIDGE</div><address class="addr">412 LINDEN AVE STE B<br>RIVERTON, LA 70100<br>P: 555.010.2311<br>F: 555.010.9725</address></header>
    <h2 class="title">FILING A CLAIM</h2>
    <ol>
      <li>Call your insurance company to set up the claim. Your date of loss is the following: date: ______________</li>
      <li>When you call in your claim, you will be given a claim number and be assigned an adjuster. Record this information below, including your adjuster's first and last name.<br>Claim Number: ______________<br>Adjuster's Name: ______________<br>Contact: ______________</li>
      <li>Typically, the adjuster will call back in 3-5 business days to schedule an inspection. Once they do so, give them my name and number and ask them to contact me to schedule the inspection.</li>
      <li>When the adjuster gives you a date and time for the inspection, record the information below and contact me immediately afterward so I can prepare.<br>Inspection Date: __________ Time: ________</li>
      <li>The only way to make sure you are fairly represented during the inspection is to make sure I am present. Please contact me as soon as you get this information.<br>Claims Specialist: ______________<br>Contact: ______________</li>
    </ol>
  </div>
</section>

<section class="page" style="left:604px;top:56px;height:231px">
  <div class="sheet">
    <header class="head" style="height:16px"><div class="brand"><span class="mark"></span>HARBOR RIDGE</div><address class="addr">412 LINDEN AVE STE B<br>RIVERTON, LA 70100<br>P: 555.010.6968<br>F: 555.010.9725</address></header>
    <div style="display:flex;justify-content:space-between;align-items:flex-end;margin-top:2px">
      <h2 style="font-size:4.6px;font-weight:400;letter-spacing:.4px;line-height:1.2">PROPOSAL<br>ESTIMATE</h2>
      <div class="lined" style="width:46px"><span>PROPOSAL #:</span><span></span><span>DATE:</span><span></span></div>
    </div>
    <div style="display:flex;gap:4px;margin-top:3px">
      <div class="box" style="flex:1;height:22px"><div class="band">PROPOSAL FOR:</div></div>
      <div class="lined" style="flex:1.1;height:17px"><span>PROJECT/JOB:</span><span></span><span>REPRESENTATIVE:</span><span></span><span>EMAIL:</span><span></span><span>CONTACT:</span><span></span></div>
    </div>
    <div class="box" style="margin-top:3px;height:90px;position:relative"><div class="band">DESCRIPTION</div>
      <div style="position:absolute;left:0;right:0;top:13px;border-top:.4px solid var(--rule)"></div>
      <div style="position:absolute;left:0;right:0;top:52px;border-top:.4px solid var(--rule)"></div>
      <div style="position:absolute;left:0;right:0;top:80px;border-top:.4px solid var(--rule)"></div>
      <div style="position:absolute;left:68%;top:4px;bottom:0;border-left:.4px solid var(--rule)"></div>
    </div>
    <p style="margin-top:2px">All material is guaranteed to be as specified. All work to be completed in a workmanlike manner according to standard practices. Any alteration or deviation from specifications involving extra costs will be executed only upon written orders. Owner to carry fire and other necessary insurance.</p>
    <div class="sig" style="margin-top:6px"><div>Homeowner</div><div>Harbor Ridge Roofing</div><div style="height:7px">Date</div><div style="height:7px">Date</div></div>
    <p class="note">Note: This proposal may be withdrawn by us if not accepted within 30 days.</p>
  </div>
</section>

<section class="page" style="left:791px;top:56px;height:231px">
  <div class="sheet">
    <header class="head"><div class="brand"><span class="mark"></span>HARBOR RIDGE</div><address class="addr">412 LINDEN AVE STE B<br>RIVERTON, LA 70100<br>P: 555.010.6968<br>F: 555.010.4477</address></header>
    <h2 class="title" style="margin:8px 0 4px">FOR THE CUSTOMER:</h2>
    <h3 class="sub">IMPORTANT THINGS TO KNOW WHEN REPLACING YOUR ROOF</h3>
    <p>If there is one home improvement that will create a dramatic enhancement to your house, it is changing your roof. You may be asking yourself what should I be preparing for and what should I expect?</p>
    <p class="blue">HERE IS A LIST OF THINGS THAT WILL HELP YOUR ROOF REPLACEMENT GO AS SMOOTHLY AS POSSIBLE:</p>
    <ol>
      <li><b>Cut your grass short:</b> When our roofers show up they will place tarps around your home to catch debris. Short grass makes it easier for us to spot and pick up any stray nails.</li>
      <li><b>Not all nails will be found:</b> Thousands of nails will be falling off the side of your roof. We sweep with a magnetic roller, but we recommend you walk around your house after the job.</li>
      <li><b>Cover items in your attic:</b> Gaps between attic boards may let dust, granules and nails fall through. Please cover stored items with tarps or sheets.</li>
      <li><b>Remove valuable art from the walls:</b> Banging from the roof might cause decorations to fall if not securely fastened.</li>
      <li><b>Satellite dishes and antennas:</b> Contact your satellite provider before the start of the job. We are not responsible for recalibrating or reinstalling the dish.</li>
    </ol>
    <span class="pnum">1</span>
  </div>
</section>

<section class="page" style="left:977px;top:56px;height:231px">
  <div class="sheet">
    <ol start="6" style="margin-top:4px">
      <li><b>Stack Pipes:</b> Your home has at least one vent called a stack pipe. We recommend a metal jack with a rubber collar to keep squirrels and weather out.</li>
      <li><b>Inform your neighbors:</b> Putting on a new roof can be loud, so let your neighbor know that it will be temporary.</li>
      <li><b>Weather is unpredictable:</b> We do not start a roof replacement during inclement weather. We keep tarps handy in case rain starts in the middle of a job.</li>
      <li><b>Decking issues:</b> Decking rots over time and sometimes cannot be seen until shingles are removed. Replacement decking is billed at a fair, fixed rate.</li>
      <li><b>Leave for the day and take your pets with you:</b> We want to guarantee everyone's safety while we complete the job. Noise and falling debris can upset animals.</li>
      <li><b>Plants might get damaged:</b> We do our best to keep your plants protected by covering them with tarps, but we cannot be responsible for damage to garden beds.</li>
      <li><b>Problems can happen:</b> While this list describes problems that have a possibility of happening, it is not often we run into them. Please be patient and keep an open line of communication.</li>
    </ol>
    <p style="margin-top:4px">Thank you,</p>
    <p>The Team at Harbor Ridge</p>
    <p class="blue" style="text-align:center;margin-top:8px">THANK YOU FOR CHOOSING HARBOR RIDGE ROOFING!</p>
    <span class="pnum">2</span>
  </div>
</section>

<!-- Row 2 -->
<section class="page mat" style="left:44px;top:296px;height:293px">
  <div class="sheet">
    <header class="head"><div class="brand"><span class="mark"></span>HARBOR RIDGE</div><address class="addr">412 LINDEN AVE STE B<br>RIVERTON, LA 70100<br>P: 555.010.6968<br>F: 555.010.4477</address></header>
    <h2 class="title" style="margin:4px 0 5px">MATERIAL ORDER FORM</h2>
    <p>Order Date: __________ Salesman: Sam __________</p>
    <p>Delivery Date: ________ Time: ______ Roof Load: ______ Pickup: ______</p>
    <p>Supply Company: ▣ Northline ☐ Gulf Supply ☐ Crestway ☐ Summit ☐ Baylor</p>
    <p>Homeowner: ______________________ Phone: ______________</p>
    <p>Address / City / State / Zip: ______________________________</p>
    <table style="margin-top:4px">
      <tr><th>SHINGLES</th><th>SQUARES</th><th>BNDLS</th><th>MANUFACTURER</th><th>TYPE</th><th>COLOR</th></tr>
      <tr><td><b>Field</b></td><td></td><td></td><td></td><td></td><td></td></tr>
      <tr><td>Ridge LF</td><td></td><td></td><td></td><td></td><td></td></tr>
      <tr><td>Starter LF</td><td></td><td></td><td></td><td></td><td></td></tr>
      <tr><td>Total Initial =</td><td></td><td></td><td></td><td></td><td></td></tr>
      <tr><td>Extra Sent Out +</td><td></td><td></td><td></td><td></td><td></td></tr>
      <tr><td>Returned -</td><td></td><td></td><td></td><td></td><td></td></tr>
      <tr><td>Total Final =</td><td></td><td></td><td></td><td></td><td></td></tr>
    </table>
    <div class="band" style="margin:6px 0 5px;border:.4px solid var(--rule)">MATERIALS</div>
    <p><b>Felt in Rolls:</b> 15LB ______ 30LB ______ Synthetic ______</p>
    <p><b>Plastic Caps:</b> ________ # of Boxes</p>
    <p><b>Gun Nails:</b> ________ # of Boxes 1" ________ # of Boxes 1¼"</p>
    <p><b>Valley Metal:</b> ________ # of LF</p>
    <p><b>Drip Edge:</b> ________ # of LF Color: __________</p>
    <p><b>Decking:</b> ________ # of Sheets ½" CDX ________ # of Sheets OSB</p>
    <p><b>Wind Turbines:</b> # ______ Color: ___Black ___Brown ___Mill</p>
    <p><b>Turtle Vents:</b> # ______ Color: ___Black ___Brown ___Mill</p>
    <p><b>Power Vent:</b> # ______ Color: ___Black ___Brown ___Mill</p>
    <p><b>Ridge Vent:</b> Aluminum ______ # of LF Nail over ______ # of LF</p>
    <p><b>Pipe Jacks:</b> ______ # of units Lead ______ 3 in 1 w/Aluminum Base ______</p>
    <p><b>Furnace Vent Cap:</b> 3" ______ 4-6" ______ 6-8" ______ # of units</p>
    <p><b>Silicone:</b> ______ # of Tubes</p>
    <p><b>Paint:</b> ______ # of Cans Color: __________</p>
    <p><b>Ice and Water Shield:</b> ______ # of Rolls</p>
    <span class="pnum">1</span>
  </div>
</section>

<section class="page" style="left:231px;top:296px;height:293px">
  <div class="sheet">
    <header class="head"><div class="brand"><span class="mark"></span>HARBOR RIDGE</div><address class="addr">412 LINDEN AVE STE B<br>RIVERTON, LA 70100<br>P: 555.010.2311<br>F: 555.010.9725</address></header>
    <div style="display:flex;justify-content:space-between;align-items:flex-end;margin-top:4px">
      <h2 style="font-size:4.6px;font-weight:400;letter-spacing:.5px">ROOFING PROPOSAL</h2>
      <div class="lined" style="width:48px"><span>PROPOSAL #:</span><span></span><span>DATE:</span><span></span></div>
    </div>
    <div style="display:flex;gap:4px;margin-top:4px">
      <div class="box" style="flex:1;height:22px"><div class="band">PROPOSAL FOR:</div></div>
      <div class="lined" style="flex:1.1;height:21px"><span>PROJECT/JOB:</span><span></span><span>REPRESENTATIVE:</span><span></span><span>EMAIL:</span><span></span><span>CONTACT:</span><span></span><span>DATE OF LOSS:</span><span></span></div>
    </div>
    <div class="box" style="margin-top:5px;height:128px;position:relative"><div class="band">DESCRIPTION</div>
      <div style="position:absolute;left:0;right:0;top:14px;border-top:.4px solid var(--rule)"></div>
      <div style="position:absolute;left:0;right:0;top:68px;border-top:.4px solid var(--rule)"></div>
      <div style="position:absolute;left:0;right:0;top:118px;border-top:.4px solid var(--rule)"></div>
      <div style="position:absolute;left:66%;top:4px;bottom:0;border-left:.4px solid var(--rule)"></div>
    </div>
    <p style="margin-top:2px">All material is guaranteed to be as specified. All work to be completed in a workmanlike manner according to standard practices. Any alteration or deviation from specifications involving extra costs will be executed only upon written orders. Owner to carry fire and other necessary insurance. Our workers are fully covered by workman's compensation insurance.</p>
    <div class="sig" style="margin-top:10px"><div>Homeowner</div><div>Harbor Ridge Roofing</div><div>Date</div><div>Date</div></div>
    <p class="note" style="margin-top:6px">Note: This proposal may be withdrawn by us if not accepted within 30 days.</p>
  </div>
</section>

<section class="page" style="left:417px;top:296px;height:293px">
  <div class="sheet">
    <header class="head"><div class="brand"><span class="mark"></span>HARBOR RIDGE</div><address class="addr">412 LINDEN AVE STE B<br>RIVERTON, LA 70100<br>P: 555.010.6968<br>F: 555.010.9725</address></header>
    <h2 class="title" style="margin:8px 0 6px">CONSTRUCTION AGREEMENT</h2>
    <p>On this date ______________, let it be known that the homeowner(s) ______________, [Homeowner], of the property located at ______________ and Harbor Ridge Roofing, otherwise known as [Harbor Ridge], located at 412 Linden Ave Ste B, Riverton, LA 70100 have entered into a contract to undergo building and or repairs specified on the proposal estimate supplied to the homeowner. Total $ __________</p>
    <div class="field" style="margin:4px 0 6px"></div>
    <p><b>SECTION 1. ACKNOWLEDGEMENT</b><br>1.1 Harbor Ridge is an independent contractor licensed and insured in the state of Louisiana and specializes in residential construction. Harbor Ridge acts on its own behalf and is not affiliated with any insurance company.</p>
    <p><b>SECTION 2. PAYMENT</b><br>2.1 The contract amount for work to be completed by Harbor Ridge will be determined by the pre agreed upon pricing in the provided proposal estimate.<br>2.2 A deposit of 50% of the contract amount will be given before any work begins. The balance is due upon completion of the job.<br>2.3 Payments shall be mailed directly to the main office or hand-delivered to a representative.</p>
    <p><b>SECTION 3. INSURANCE SUPPLEMENTS</b><br>3.1 All supplements requested by Harbor Ridge on behalf of the insured for additional damages discovered are to be paid by the property owner's insurance company.<br>3.2 The insured agrees to have all work stated on the supplemental loss sheet started or scheduled within 15 days of receiving funds.</p>
    <p><b>SECTION 4. AUTHORIZATION</b><br>4.1 I authorize Harbor Ridge to supply information regarding the claim to my insurance company.<br>4.2 In the event that Harbor Ridge is not allowed to perform its recommended procedures, I agree to release and hold Harbor Ridge harmless.</p>
    <p><b>THIS SUBCONTRACT AGREEMENT IS ACKNOWLEDGED AND EXECUTED AS OF THE DATE SET FORTH ABOVE BY:</b></p>
    <div class="sig" style="margin-top:6px;grid-template-columns:1.6fr 1fr"><div style="height:10px">Homeowner Signature</div><div style="height:10px">Date</div><div style="height:10px">Homeowner Signature</div><div style="height:10px">Date</div><div style="height:10px">Harbor Ridge Signature</div><div style="height:10px">Date</div></div>
    <span class="pnum">1</span>
  </div>
</section>

<section class="page" style="left:604px;top:296px;height:293px">
  <div class="sheet">
    <p class="notice-top">Federal law requires that we give you the following notice of lien rights afforded to persons or companies furnishing labor or materials for the improvement of real property.</p>
    <h2 class="title" style="margin:2px 0 5px">NOTICE</h2>
    <p><b>NOTICE OF CANCELLATION – YOU, THE BUYER, MAY CANCEL THIS PURCHASE ANY TIME PRIOR TO MIDNIGHT OF THE THIRD BUSINESS DAY AFTER THE DATE OF THIS PURCHASE IN WRITING.</b></p>
    <ol>
      <li>It is agreed that the amount of the contract shall be the amount equal to the value as stated on the proposal.</li>
      <li>Our company has the right to order excess material. These materials will not be charged to the customer.</li>
      <li>Additional labor and materials needed beyond the original scope of work shall be paid directly to the company.</li>
      <li>All material is guaranteed to be as specified. All work is to be completed in a workmanlike manner according to standard practices.</li>
      <li>This agreement constitutes the entire agreement between the parties. It may be changed only by written instrument.</li>
      <li>If any provision of this agreement should be held invalid, the remaining provisions shall not be affected.</li>
      <li>Any representation or statement not written in this contract is agreed to be immaterial.</li>
      <li>If the customer cancels this contract later than three days from execution, the customer shall pay twenty-five percent of the contract price.</li>
      <li>All accepted proposals are subject to approval of our credit department and management.</li>
      <li>The company is not responsible for any damage, pre-existing or future construction defects caused by storms or lack of maintenance.</li>
      <li>Should default be made in payment, interest charges shall be added at a rate of eight percent per annum.</li>
      <li>The above conditions shall be considered a part of this contract.</li>
      <li>Homeowners agreement to the contingency statement shall be considered a part of this contract.</li>
      <li>The dollar amount of the contract is the amount agreed upon by the homeowner and the insurance company.</li>
      <li>The final payment in full shall not be held up while waiting for the city to inspect the work.</li>
    </ol>
    <span class="pnum">2</span>
  </div>
</section>

<section class="page" style="left:791px;top:296px;height:293px">
  <div class="sheet">
    <header class="head"><div class="brand"><span class="mark"></span>HARBOR RIDGE</div><address class="addr">412 LINDEN AVE STE B<br>RIVERTON, LA 70100<br>P: 555.010.6968<br>F: 555.010.9725</address></header>
    <h2 class="title" style="margin:6px 0 6px">CONSTRUCTION AGREEMENT</h2>
    <p>On this date ______________, let it be known that the insured homeowner(s) ______________, [Homeowner], of the property located at ______________ and Harbor Ridge Roofing, otherwise known as [Harbor Ridge], located at 412 Linden Ave Ste B, Riverton, LA 70100 have entered into a contract to repair or replace the damaged roof as specified on the insurance loss sheet. Total $ __________</p>
    <div class="row" style="gap:6px;margin-top:5px"><div><div class="field"></div><div class="label">Policy Number</div></div><div><div class="field"></div><div class="label">Claim Number</div></div><div><div class="field"></div><div class="label">Date of Loss</div></div></div>
    <div class="row" style="gap:6px;margin-bottom:5px"><div><div class="field"></div><div class="label">Mortgage Company</div></div><div><div class="field"></div><div class="label">Loan Number</div></div></div>
    <p><b>SECTION 1. ACKNOWLEDGEMENT</b><br>1.1 Harbor Ridge is an independent contractor licensed and insured in the state of Louisiana and specializes in the reconstruction of damaged structures.</p>
    <p><b>SECTION 2. PAYMENT</b><br>2.1 The contract amount for work to be completed will be determined by the homeowner's loss sheet provided by their insurance company.<br>2.2 A deposit of 30% of the contract amount will be given before any work begins. The balance is due upon completion of the job.<br>2.3 Payments shall be mailed directly to the main office or hand-delivered to a representative.</p>
    <p><b>SECTION 3. INSURANCE SUPPLEMENTS</b><br>3.1 All supplements requested on behalf of the insured for additional damages are to be paid by the property owner's insurance company.<br>3.2 The insured agrees to have all work stated on the supplemental loss sheet scheduled within 15 days.</p>
    <p><b>SECTION 4. AUTHORIZATION</b><br>4.1 I authorize Harbor Ridge to supply information regarding the claim to my insurance company.<br>4.2 If Harbor Ridge is not allowed to perform its recommended procedures, I agree to hold Harbor Ridge harmless.</p>
    <p><b>THIS SUBCONTRACT AGREEMENT IS ACKNOWLEDGED AND EXECUTED AS OF THE DATE SET FORTH ABOVE BY:</b></p>
    <div class="sig" style="margin-top:6px;grid-template-columns:1.6fr 1fr"><div style="height:10px">Homeowner Signature</div><div style="height:10px">Date</div><div style="height:10px">Homeowner Signature</div><div style="height:10px">Date</div><div style="height:10px">Harbor Ridge Signature</div><div style="height:10px">Date</div></div>
    <span class="pnum">1</span>
  </div>
</section>

<section class="page" style="left:977px;top:296px;height:293px">
  <div class="sheet">
    <p class="notice-top">Federal law requires that we give you the following notice of lien rights afforded to persons or companies furnishing labor or materials for the improvement of real property.</p>
    <h2 class="title" style="margin:2px 0 5px">NOTICE</h2>
    <p><b>NOTICE OF CANCELLATION – YOU, THE BUYER, MAY CANCEL THIS PURCHASE ANY TIME PRIOR TO MIDNIGHT OF THE THIRD BUSINESS DAY AFTER THE DATE OF THIS PURCHASE IN WRITING.</b></p>
    <ol>
      <li>It is agreed that the amount of the contract shall be the amount equal to the replacement cost value.</li>
      <li>Our roofing company has the right to order excess material. These materials will not be charged.</li>
      <li>Additional labor and materials beyond the original scope of repairs shall be paid directly to the company.</li>
      <li>All material is guaranteed to be as specified. All work is to be completed in a workmanlike manner according to standard practices.</li>
      <li>This agreement constitutes the entire agreement between the parties. It may be changed only by written instrument.</li>
      <li>If any provision of this agreement should be held invalid, the remaining provisions shall not be affected.</li>
      <li>Any representation or statement not written in this contract is agreed to be immaterial.</li>
      <li>If the customer cancels this contract later than three days from execution, the customer shall pay twenty-five percent of the replacement cost value.</li>
      <li>All accepted proposals are subject to approval of our credit department and management.</li>
      <li>The company is not responsible for any damage below the roof due to leaks by wind, ice dams or hail.</li>
      <li>Should default be made in payment, interest charges shall be added at a rate of eight percent per annum.</li>
      <li>The above conditions shall be considered a part of this contract.</li>
      <li>Homeowners agreement to the contingency statement shall be considered a part of this contract.</li>
      <li>The dollar amount of the contract is the amount agreed upon by the homeowner and the insurance company.</li>
      <li>The final payment in full shall not be held up while waiting for the city to inspect the work.</li>
    </ol>
    <span class="pnum">2</span>
  </div>
</section>

<!-- Row 3 -->
<section class="page" style="left:44px;top:600px;height:231px">
  <div class="sheet">
    <header class="head"><div class="brand"><span class="mark"></span>HARBOR RIDGE</div><address class="addr">412 LINDEN AVE STE B<br>RIVERTON, LA 70100<br>P: 555.010.2311<br>F: 555.010.9725</address></header>
    <h2 class="title" style="margin:8px 0 8px">CUSTOMER INFORMATION</h2>
    <div class="row" style="gap:20px"><div style="flex:3"><div class="field"></div><div class="label">Name</div></div><div><div class="field"></div><div class="label">Last 4 Digits of SSN</div></div></div>
    <div><div class="field" style="margin-top:4px"></div><div class="label">Address</div></div>
    <div class="row" style="gap:8px"><div><div class="field" style="margin-top:4px"></div><div class="label">City</div></div><div><div class="field" style="margin-top:4px"></div><div class="label">State</div></div><div><div class="field" style="margin-top:4px"></div><div class="label">Zip</div></div></div>
    <div class="row" style="gap:8px"><div><div class="field" style="margin-top:4px"></div><div class="label"><b>Telephone</b></div></div><div><div class="field" style="margin-top:4px"></div><div class="label">Email Address</div></div></div>
    <div style="border-top:.4px solid #d9a89a;margin:14px 0 4px"></div>
    <div class="row" style="gap:8px"><div><div class="field" style="margin-top:4px"></div><div class="label">Insurance Company</div></div><div><div class="field" style="margin-top:4px"></div><div class="label">Claim #</div></div></div>
    <div class="row" style="gap:8px"><div></div><div><div class="field" style="margin-top:2px"></div><div class="label">Policy #</div></div></div>
    <div class="row" style="gap:8px"><div><div class="field" style="margin-top:4px"></div><div class="label">Insurance Adjuster</div></div><div><div class="field" style="margin-top:4px"></div><div class="label">Contact</div></div></div>
    <div class="row" style="gap:8px"><div><div class="field" style="margin-top:10px"></div><div class="label">Mortgage Company</div></div><div><div class="field" style="margin-top:10px"></div><div class="label">Loan #</div></div></div>
    <div class="row" style="gap:8px"><div></div><div><div class="field" style="margin-top:2px"></div><div class="label">Tracking #</div></div></div>
  </div>
</section>

<section class="page" style="left:231px;top:600px;height:231px">
  <div class="sheet">
    <header class="head"><div class="brand"><span class="mark"></span>HARBOR RIDGE</div><address class="addr">412 LINDEN AVE STE B<br>RIVERTON, LA 70100<br>P: 555.010.2311<br>F: 555.010.9725</address></header>
    <h2 class="title" style="margin:8px 0 8px">CLIENT GUARANTEE</h2>
    <p style="text-align:justify">Harbor Ridge Roofing will invest its time and expertise in assisting the client with their insurance claim. This proposal is contingent upon the insurance company paying for the damages and will be voided only if the claim is disallowed by the insurance company. The client and Harbor Ridge Roofing will not be obligated unless the repairs are approved by the client's insurance company. The client agrees to let Harbor Ridge Roofing do the work specified for the roof replacement or repair on the insurance loss sheet for the replacement cost, overhead, profit and material taxes. Harbor Ridge Roofing reserves the right to supplement the insurance company for additional costs. There will be no additional cost to the client. The client's expense will not exceed the deductible amount unless the homeowner has an ACV policy.</p>
    <div class="sig" style="margin-top:42px"><div>Client</div><div>Harbor Ridge Roofing</div><div>Date</div><div>Date</div></div>
  </div>
</section>

<section class="page" style="left:417px;top:600px;height:231px">
  <div class="sheet">
    <header class="head"><div class="brand"><span class="mark"></span>HARBOR RIDGE</div><address class="addr">412 LINDEN AVE STE B<br>RIVERTON, LA 70100<br>P: 555.010.2311<br>F: 555.010.9725</address></header>
    <h2 class="title" style="margin:8px 0 8px">THIRD PARTY AUTHORIZATION FORM</h2>
    <p>Re: &nbsp;&nbsp;Claim#: ____________________</p>
    <p>&nbsp;&nbsp;&nbsp;&nbsp;&nbsp;&nbsp;&nbsp;Loan#: ____________________</p>
    <p style="margin-top:5px">To Whom It May Concern:</p>
    <p style="margin-top:3px">I do hereby authorize ______________________________ (my lender/mortgage servicer) and ______________________________ (my insurance company) to release, or otherwise provide, any and all information to Harbor Ridge Roofing as well as allow the third party to act on my behalf in regard to the above mentioned loan number for insurance claim number for my property located at:</p>
    <div><div class="field" style="margin-top:6px"></div><div class="label">Address</div></div>
    <div class="row" style="gap:8px"><div><div class="field" style="margin-top:4px"></div><div class="label">City</div></div><div><div class="field" style="margin-top:4px"></div><div class="label">State</div></div><div><div class="field" style="margin-top:4px"></div><div class="label">Zip</div></div></div>
    <div class="row" style="gap:8px"><div><div class="field" style="margin-top:14px"></div><div class="label">Printed Borrower Name</div></div><div><div class="field" style="margin-top:14px"></div><div class="label">Borrower Signature</div></div><div><div class="field" style="margin-top:14px"></div><div class="label">Date</div></div></div>
    <div class="row" style="gap:8px"><div><div class="field" style="margin-top:6px"></div><div class="label">Printed Borrower Name</div></div><div><div class="field" style="margin-top:6px"></div><div class="label">Borrower Signature</div></div><div><div class="field" style="margin-top:6px"></div><div class="label">Date</div></div></div>
  </div>
</section>

</body>
</html>
```